Need a Brochure Design

We need a brochure designed (A4 two sides or A3 foldable which is equal to 2 x A4 = total of four pages )

Brief and Logo attached.

```html
<!DOCTYPE html>
<html lang="en">
<head>
<meta charset="utf-8">
<title>Nestwell Styling – Brochure</title>
<link href="https://fonts.googleapis.com/css2?family=Raleway:wght@400;500;600;700&family=Oswald:wght@500;600&family=Montserrat:wght@500;600;700&display=swap" rel="stylesheet">
<style>
:root{
  --orange:#ef8640;
  --orange-soft:#f6a26a;
  --charcoal:#2b2e31;
  --peach:#fce6d3;
  --peach-light:#fdf3ea;
  --ink:#1d1d1d;
  --grey-text:#555;
  --stage:#8c8c8a;
  --white:#ffffff;
}
*{box-sizing:border-box;margin:0;padding:0}
html,body{width:1200px;height:856px;overflow:hidden;background:var(--stage)}
body{position:relative;font-family:'Raleway',sans-serif;color:var(--ink)}
.page{position:absolute;top:39px;width:550px;height:778px;background:var(--white);overflow:hidden}
.page--front{left:34px;background:linear-gradient(180deg,var(--white) 55%,var(--peach-light) 80%,var(--peach) 100%)}
.page--back{left:616px;background:linear-gradient(180deg,var(--white) 10%,var(--peach-light) 60%,var(--white) 90%)}
.abs{position:absolute}
.photo{position:absolute}

/* front */
.hero{left:0;top:0;width:550px;height:226px;background:linear-gradient(160deg,#e9e6e1 0%,#d7cbbd 45%,#9c7a55 75%,#5b4532 100%)}
.brand-tab{left:42px;top:0;width:110px;height:114px;background:var(--white);border-radius:0 0 55px 55px;display:flex;align-items:center;justify-content:center}
.brand-name{font-family:'Raleway',sans-serif;font-weight:600;font-size:13px;color:var(--charcoal);text-align:center;line-height:1.2}
.tagline-band{left:0;top:226px;width:550px;height:31px;background:var(--orange)}
.tagline{left:32px;top:229px;font-family:'Oswald',sans-serif;font-weight:600;font-size:17px;color:var(--white);letter-spacing:.3px}
.intro-panel{left:0;top:257px;width:550px;height:155px;background:var(--charcoal)}
.team-photo{left:313px;top:231px;width:218px;height:218px;border-radius:50%;border:4px solid var(--white);background:radial-gradient(circle at 50% 60%,#f1eeea 0%,#cfcac3 55%,#8f8a84 100%)}
.owner-photo{left:30px;top:274px;width:64px;height:64px;border-radius:50%;border:2px solid var(--white);background:linear-gradient(160deg,#d9d6d2,#8b8682)}
.greeting{left:101px;top:280px;font-size:13px;font-weight:500;color:var(--orange)}
.greeting-text{left:101px;top:298px;width:196px;font-size:7.6px;line-height:11px;color:var(--white);text-align:justify}
.intro-text{left:35px;top:346px;width:270px;font-size:7.6px;line-height:11px;color:var(--white)}
.section-title{font-family:'Raleway',sans-serif;font-weight:500;font-size:10.5px;color:var(--ink);letter-spacing:.2px}
.body{font-size:7.4px;line-height:11px;color:var(--grey-text)}
.impressions-title{left:33px;top:427px}
.impressions-text{left:33px;top:450px;width:488px}
.impressions-text p{margin-bottom:4px}
.connected-title{left:33px;top:537px}
.connected-text{left:35px;top:561px;width:190px;text-align:justify}
.why-title{left:280px;top:537px}
.why-list{left:280px;top:557px;list-style:none}
.why-list li{font-size:7.4px;line-height:13px;color:var(--grey-text);display:flex;align-items:center;gap:5px}
.referral-title{left:31px;top:652px}
.offer-big{left:31px;top:666px;font-family:'Raleway',sans-serif;font-weight:500;font-size:38px;line-height:38px;color:var(--ink)}
.offer-voucher{left:31px;top:704px;font-family:'Oswald',sans-serif;font-weight:600;font-size:20px;color:var(--orange)}
.offer-foot{left:31px;top:729px;font-family:'Oswald',sans-serif;font-weight:500;font-size:12.5px;color:var(--ink)}
.contact-title{left:274px;top:645px;font-size:10.5px;line-height:12px;font-weight:500}
.phone-line{display:flex;align-items:center;gap:4px;font-family:'Montserrat',sans-serif;font-weight:700;color:var(--ink)}
.front-phone{left:273px;top:677px;font-size:18px}
.front-email{left:273px;top:698px;font-size:9px;color:var(--ink)}
.web-title{left:273px;top:716px;font-size:10.5px;font-weight:500}
.front-web{left:273px;top:733px;font-size:12.5px;font-family:'Montserrat',sans-serif;font-weight:600;display:flex;align-items:center;gap:4px}
.front-footer{left:0;top:771px;width:550px;height:7px;background:var(--orange)}

/* back */
.headline-band{left:0;top:0;width:550px;height:76px;background:var(--orange)}
.headline{left:0;top:20px;width:550px;text-align:center;font-size:14.5px;line-height:16px;color:var(--ink)}
.headline strong{font-weight:700}
.price-table{left:33px;top:63px;width:485px;border-collapse:collapse;font-family:'Montserrat',sans-serif}
.price-table th{background:var(--charcoal);color:var(--orange);height:28px;font-weight:600;font-size:8.5px}
.price-table th.plan-head{font-size:13px;text-align:left;padding-left:40px;font-weight:700}
.price-table td{height:42px;border:1px solid var(--charcoal);text-align:center;background:rgba(255,255,255,.35)}
.price-table td.plan{text-align:left;padding-left:28px}
.plan-name{font-size:14px;font-weight:600;display:block;line-height:15px}
.plan-detail{font-size:7px;font-weight:600;display:block}
.price-sale{color:var(--orange);font-weight:700;font-size:12px}
.price-was{text-decoration:line-through;font-size:11.5px;color:#333}
.sale-tag{color:var(--orange);font-size:10.5px;font-family:'Raleway',sans-serif}
.col-plan{width:218px}.col-sale{width:98px}.col-was{width:102px}
.table-note{left:52px;top:263px;font-size:7px;color:var(--ink);background:var(--white);padding:0 3px}
.gallery-wide{left:31px;top:294px;width:319px;height:118px;background:linear-gradient(170deg,#f4f2ef 0%,#dcd8d2 55%,#b8b1a8 100%)}
.gallery-tall{left:356px;top:294px;width:162px;height:236px;background:linear-gradient(160deg,#ece7e1 0%,#c2b8ad 50%,#6d7180 100%)}
.gallery-a{left:31px;top:419px;width:156px;height:111px;background:linear-gradient(170deg,#efebe7 0%,#cfc9c2 60%,#545457 100%)}
.gallery-b{left:195px;top:419px;width:155px;height:111px;background:linear-gradient(170deg,#f2efec 0%,#d9d3d0 55%,#d9b7b6 100%)}
.benefits{left:33px;top:554px;list-style:none}
.benefits li{font-size:9.6px;line-height:14.8px;color:#333;display:flex;align-items:center;gap:7px}
.brand-mark{left:380px;top:640px;width:150px;height:150px;border-radius:50%;background:var(--peach);opacity:.75}
.brand-mark-name{left:380px;top:700px;width:150px;text-align:center;font-size:17px;font-weight:500;color:var(--charcoal)}
.back-contact-title{left:29px;top:664px;font-size:13px;color:var(--orange);font-weight:500}
.back-phone{left:29px;top:679px;font-size:22px}
.back-email{left:29px;top:706px;font-size:7.6px;letter-spacing:.2px}
.social{left:233px;top:699px;display:flex;gap:3px}
.social span{width:13px;height:13px;border-radius:50%;background:var(--orange)}
.back-footer{left:0;top:737px;width:550px;height:41px;background:var(--charcoal);display:flex;align-items:center;justify-content:center;font-family:'Montserrat',sans-serif;font-size:13px;letter-spacing:1.4px;color:var(--white)}
.back-footer b{color:var(--orange);font-weight:700}
</style>
</head>
<body>

<svg width="0" height="0" style="position:absolute">
  <defs>
    <symbol id="icon-tick" viewBox="0 0 12 12"><circle cx="6" cy="6" r="6" fill="#ef8640"/><path d="M3.2 6.2l2 2 3.8-4" fill="none" stroke="#fff" stroke-width="1.6" stroke-linecap="round" stroke-linejoin="round"/></symbol>
    <symbol id="icon-tick-line" viewBox="0 0 12 12"><circle cx="6" cy="6" r="5" fill="none" stroke="#ef8640" stroke-width="1.2"/><path d="M3.5 6l2 2 4.5-5" fill="none" stroke="#ef8640" stroke-width="1.4" stroke-linecap="round"/></symbol>
    <symbol id="icon-phone" viewBox="0 0 20 20"><path d="M5 2.5l3 .3 1 4-2 1.5c1 2.2 2.5 3.8 4.7 4.8l1.5-2 4 1 .3 3c-.3 1.5-1.5 2.4-3 2.2C8.6 16.6 3.4 11.4 2.8 5.5 2.6 4 3.5 2.8 5 2.5z" fill="none" stroke="currentColor" stroke-width="1.6" stroke-linejoin="round"/></symbol>
    <symbol id="icon-globe" viewBox="0 0 20 20"><circle cx="10" cy="10" r="8" fill="none" stroke="#ef8640" stroke-width="1.5"/><ellipse cx="10" cy="10" rx="3.5" ry="8" fill="none" stroke="#ef8640" stroke-width="1.3"/><path d="M2 10h16M3.5 6h13M3.5 14h13" stroke="#ef8640" stroke-width="1.2"/></symbol>
  </defs>
</svg>

<!-- Front page -->
<section class="page page--front">
  <div class="photo hero" role="img" aria-label="Photo of a styled open-plan kitchen and dining room with a timber table"></div>
  <div class="abs brand-tab"><span class="brand-name">Nestwell<br>Styling</span></div>

  <div class="abs tagline-band"></div>
  <h1 class="abs tagline">FLEXIBLE &amp; AFFORDABLE PROPERTY STYLING</h1>

  <div class="abs intro-panel"></div>
  <div class="photo owner-photo" role="img" aria-label="Portrait photo of the owner and creative director"></div>
  <h2 class="abs greeting">HEY THERE,</h2>
  <p class="abs greeting-text">I'm Mara, Owner and Creative Director of Nestwell Styling. Please let me introduce you to our amazingly creative property styling team!</p>
  <p class="abs intro-text">We are a friendly bunch who are passionate about home staging. We've been property staging apartments, townhouses, and stand-alone homes since 2009. An all-female powerhouse, we combine our experience in art, interior design, retail, and business to offer professional home styling throughout Melbourne.</p>
  <div class="photo team-photo" role="img" aria-label="Group photo of the styling team in a studio"></div>

  <h3 class="abs section-title impressions-title">BECAUSE FIRST IMPRESSIONS COUNT</h3>
  <div class="abs body impressions-text">
    <p>A gorgeous looking home sells faster and fetches a higher price.</p>
    <p>At Nestwell Styling, we help our property clients create a lasting impression with minimal spend. Our property vendors are usually looking for home-staging on a tight budget. They come to us searching for creative transformations to help them sell well. Thoughtfully positioned furniture and on-trend interior décor can make all the difference!</p>
    <p>Our property styling service includes a free consultation, longer rental periods, &amp; installation &amp; removal.</p>
  </div>

  <h3 class="abs section-title connected-title">WE'RE WELL-CONNECTED</h3>
  <p class="abs body connected-text">We have a steady flow of clients who have not yet secured their Real Estate Agents, so we'd be happy to share the love. We believe in last relationships, and we work with reputable agents across Melbourne.</p>

  <h3 class="abs section-title why-title">WHY CHOOSE NESTWELL STYLING?</h3>
  <ul class="abs why-list">
    <li><svg width="9" height="9"><use href="#icon-tick-line"/></svg>Experienced, enthusiastic property stylists</li>
    <li><svg width="9" height="9"><use href="#icon-tick-line"/></svg>Work with low client budgets</li>
    <li><svg width="9" height="9"><use href="#icon-tick-line"/></svg>Fast turnaround to a tight deadline</li>
    <li><svg width="9" height="9"><use href="#icon-tick-line"/></svg>Flexible rental terms (4/6/8 weeks)</li>
    <li><svg width="9" height="9"><use href="#icon-tick-line"/></svg>Happy to recommend potential customers</li>
  </ul>

  <h3 class="abs section-title referral-title">WE REWARD REFERRALS!</h3>
  <p class="abs offer-big">WE OFFER</p>
  <p class="abs offer-voucher">A $200 GIFT VOUCHER</p>
  <p class="abs offer-foot">FOR EVERY SUCCESSFUL REFERRAL TO US!</p>

  <p class="abs section-title contact-title">WE'D LOVE TO HEAR FROM YOU, SO PLEASE<br>CONTACT US BY TELEPHONE, TEXT, OR EMAIL:</p>
  <p class="abs phone-line front-phone"><svg width="14" height="14" style="color:var(--orange)"><use href="#icon-phone"/></svg>0400 318 562</p>
  <p class="abs front-email">hello@nestwellstyling.com.au</p>
  <p class="abs web-title">PLEASE ALSO VISIT OUR WEBSITE</p>
  <p class="abs front-web"><svg width="13" height="13"><use href="#icon-globe"/></svg>Nestwellstyling.com.au</p>
  <div class="abs front-footer"></div>
</section>

<!-- Back page -->
<section class="page page--back">
  <div class="abs headline-band"></div>
  <p class="abs headline">WE AVERAGE OVER 185 PROPERTY STYLING PROJECTS PER YEAR<br><strong>WITH A LARGE PROPORTION SELLING IN LESS THAN 30 DAYS!</strong></p>

  <table class="abs price-table">
    <thead>
      <tr><th class="plan-head col-plan">PLANS &amp; PRICES</th><th class="col-sale">SALE PRICE</th><th class="col-was">ORIGINAL PRICE</th><th>SALE</th></tr>
    </thead>
    <tbody>
      <tr><td class="plan"><span class="plan-name">1 Bedroom Property</span><span class="plan-detail">Full Styling &nbsp;+&nbsp; 6-8 Weeks Free Hire*</span></td><td class="price-sale">1,897.00</td><td class="price-was">2,750.00</td><td class="sale-tag">SALE</td></tr>
      <tr><td class="plan"><span class="plan-name">2 Bedroom Property</span><span class="plan-detail">Full Styling &nbsp;+&nbsp; 6-8 Weeks Free Hire*</span></td><td class="price-sale">2,697.00</td><td class="price-was">3,250.00</td><td class="sale-tag">SALE</td></tr>
      <tr><td class="plan"><span class="plan-name">3 Bedroom Property</span><span class="plan-detail">Full Styling &nbsp;+&nbsp; 6-8 Weeks Free Hire*</span></td><td class="price-sale">2,997.00</td><td class="price-was">4,470.00</td><td class="sale-tag">SALE</td></tr>
      <tr><td class="plan"><span class="plan-name">4 Bedroom Property</span><span class="plan-detail">Full Styling &nbsp;+&nbsp; 6-8 Weeks Free Hire*</span></td><td class="price-sale">3,897.00</td><td class="price-was">5,485.00</td><td class="sale-tag">SALE</td></tr>
    </tbody>
  </table>
  <p class="abs table-note">*4 Weeks Free Hire + 2 or 4 Weeks Free Extension (if property not sold within 4 weeks)</p>

  <div class="photo gallery-wide" role="img" aria-label="Photo of a bright staged living and dining area"></div>
  <div class="photo gallery-tall" role="img" aria-label="Photo of a stylist arranging cushions on a sofa"></div>
  <div class="photo gallery-a" role="img" aria-label="Photo of a staged lounge with grey sofas and a dark rug"></div>
  <div class="photo gallery-b" role="img" aria-label="Photo of stylists making up a staged bedroom"></div>

  <ul class="abs benefits">
    <li><svg width="10" height="10"><use href="#icon-tick"/></svg>Helping your property reach its highest potential without busting the budget.</li>
    <li><svg width="10" height="10"><use href="#icon-tick"/></svg>Achieving a record number of viewings &amp; the highest possible sale price.</li>
    <li><svg width="10" height="10"><use href="#icon-tick"/></svg>Installation, interior design &amp; decoration, &amp; removal included.</li>
    <li><svg width="10" height="10"><use href="#icon-tick"/></svg>Pre-sale home preparation to post-sale removal.</li>
    <li><svg width="10" height="10"><use href="#icon-tick"/></svg>Free consultation &amp; longer rental periods.</li>
    <li><svg width="10" height="10"><use href="#icon-tick"/></svg>A small investment for such a large transformation!</li>
  </ul>

  <div class="abs brand-mark"></div>
  <p class="abs brand-mark-name">Nestwell Styling</p>

  <p class="abs back-contact-title">PLEASE CONTACT US ON</p>
  <p class="abs phone-line back-phone"><svg width="16" height="16" style="color:var(--ink)"><use href="#icon-phone"/></svg>0400 318 562</p>
  <p class="abs back-email">HELLO@NESTWELLSTYLING.COM.AU</p>
  <div class="abs social"><span></span><span></span><span></span></div>

  <footer class="abs back-footer">www.<b>Nestwellstyling</b>.com.au</footer>
</section>

</body>
</html>
```